KTRV Promo Flyer for Corporate Events

Need a 8 page company overview

Target Market(s)

Creditors and Service Providers

Industry/Entity Type

Credit Card

Font styles to use
Serif

Colors
0455a3
fbf289

Requirements
Must have
• Fantastic Material and Creative
Nice to have
• Creative and personal

```html
<!DOCTYPE html>
<html lang="en">
<head>
<meta charset="utf-8">
<title>KTRV Company Overview</title>
<link rel="stylesheet" href="https://fonts.googleapis.com/css2?family=Source+Serif+4:ital,opsz,wght@0,8..60,400;0,8..60,700;1,8..60,400&display=swap">
<style>
  :root {
    --bg: #ececec;
    --paper: #ffffff;
    --teal: #0a6f86;
    --navy: #0455a3;
    --band-dark: #0a4480;
    --cyan: #0aa6d0;
    --text: #1f4f80;
    --yellow: #fbf289;
    --serif: "Source Serif 4", Georgia, serif;
  }
  * { margin: 0; padding: 0; box-sizing: border-box; }
  html, body { width: 1200px; height: 1000px; overflow: hidden; background: var(--bg); }
  body { position: relative; font-family: var(--serif); color: var(--text); }
  .page { position: absolute; width: 332px; height: 468px; background: var(--paper); overflow: hidden; }
  .page--summary { left: 94px; top: 30px; }
  .page--access { left: 444px; top: 30px; }
  .page--leadership { left: 790px; top: 30px; }
  .page--values { left: 444px; top: 510px; }

  .heading { font-weight: 700; font-size: 20px; line-height: 1; }
  .page--summary .heading { color: var(--teal); }
  .page--access .heading, .page--leadership .heading, .page--values .heading { color: var(--navy); }
  .body-text { font-size: 7.4px; line-height: 1.3; }
  .page--summary .body-text { color: var(--teal); }
  .bullets { list-style: none; font-size: 7.4px; line-height: 1.3; }
  .bullets li::before { content: "•"; }
  .page--summary .bullets { color: var(--teal); }
  .section + .section { margin-top: 12px; }
  .section .heading { margin-bottom: 3px; }

  .block { position: absolute; left: 20px; right: 18px; }

  /* summary band rows */
  .band { position: absolute; height: 34px; background: var(--cyan); }
  .band-label { position: absolute; font-weight: 700; font-size: 8.4px; line-height: 1.25; color: var(--navy); }

  /* access page */
  .access-title { font-size: 9.5px; font-weight: 700; color: var(--navy); }
  .access-quote { font-size: 7.4px; font-style: italic; line-height: 1.3; color: var(--navy); margin-top: 5px; }
  .access-band { position: absolute; left: 0; right: 0; top: 67px; height: 75px; background: var(--band-dark);
    border-bottom: 3px solid var(--yellow); }
  .spaced li { margin-bottom: 4.3px; }

  /* leadership */
  .person { margin-top: 9px; }
  .person-name { font-size: 9.5px; font-weight: 700; color: var(--navy); }
  .person-role { font-size: 6.3px; color: var(--navy); margin-bottom: 2px; }
  .page--leadership .body-text { font-size: 6.3px; line-height: 1.28; }
  .subtitle { font-size: 7.5px; color: var(--navy); }

  /* values */
  .value-badges { display: flex; gap: 12px; margin-top: 14px; align-items: center; }
  .value-badge { width: 44px; height: 30px; border-radius: 3px; }
  .value-badge--tag { background: linear-gradient(180deg, #1a8fd8 0 38%, #ffffff 38% 82%, #1a8fd8 82%);
    border: 2px solid #1a8fd8; }
  .subheading { font-size: 9.5px; font-weight: 700; color: var(--navy); }
  .contact { font-size: 9.5px; line-height: 1.3; color: var(--navy); }
  .contact strong { display: block; font-size: 10px; }
  .illustration { position: absolute; left: 0; right: 0; bottom: 0; height: 160px;
    background: linear-gradient(180deg, #ffffff 0%, #f3f5ef 25%, #dfe9ef 65%, #c9dbe6 100%); }
</style>
</head>
<body>

<section class="page page--summary">
  <div class="block" style="top:18px">
    <div class="section">
      <h1 class="heading">Executive Summary</h1>
      <p class="body-text">Kestrel Trade Recovery (KTR) is a national debt recovery agency found in 1986 and based in Seattle, Washington. We specialize in managing delinquent account receivables and we provide a range of collection services to help your business collect on past due accounts. Our goal is to proactiviley manage receivables to minimize risk by executing strategic and operational plans designed to assist our partners achieve financial expectations and stability.</p>
    </div>
    <div class="section">
      <h2 class="heading">Key Components</h2>
      <ul class="bullets">
        <li>Providing superior client service includes our "Positive Collections" approach</li>
        <li>Our conversations are based on non-confrontation approach built on coopertaiton</li>
        <li>Full compliance of all debt collection related laws</li>
      </ul>
    </div>
    <div class="section">
      <h2 class="heading">Shared Vision</h2>
      <ul class="bullets">
        <li>Outstanding customer relations</li>
        <li>It's out job to increase revenue</li>
        <li>KTR defines a quality partnership by total value we provide our clients</li>
      </ul>
    </div>
  </div>

  <div class="band" style="top:243px;left:0;width:22px"></div>
  <p class="band-label" style="top:249px;left:30px">Outstanding<br>Consumer Relations</p>
  <div class="band" style="top:243px;left:116px;right:0"></div>

  <div class="band" style="top:287px;left:0;width:174px"></div>
  <p class="band-label" style="top:293px;left:186px">Responsive<br>Client Services</p>
  <div class="band" style="top:287px;left:256px;right:0"></div>

  <div class="band" style="top:330px;left:0;width:46px"></div>
  <p class="band-label" style="top:336px;left:54px">Communications and<br>Reporting</p>
  <div class="band" style="top:330px;left:144px;right:0"></div>

  <div class="band" style="top:373px;left:0;width:224px"></div>
  <p class="band-label" style="top:379px;left:234px">Complete<br>Compliance</p>
  <div class="band" style="top:373px;left:292px;right:0"></div>

  <div class="band" style="top:417px;left:0;width:126px"></div>
  <p class="band-label" style="top:423px;left:134px">Highly Effective<br>Data Security</p>
  <div class="band" style="top:417px;left:206px;right:0"></div>
</section>

<section class="page page--access">
  <div class="block" style="top:22px">
    <h2 class="access-title">Online Access 24/7/365</h2>
    <p class="access-quote">"We believe in total transparency as a fundamental element or a true quality partnership. We give our clients online access to their accounts 24/7/365."</p>
  </div>
  <div class="access-band"></div>
  <div class="block" style="top:153px">
    <h2 class="heading">Accountability</h2>
    <p class="body-text" style="margin-top:3px">No matter how could we are – we believe that it is always room for improvement We have developed a propority system of organizational self-appraisal under categories such as</p>
    <ul class="bullets spaced" style="margin:5px 0 0 4px">
      <li>Client Satisfaction</li>
      <li>Use of resources</li>
      <li>Consumer satisfaction</li>
      <li>Complaint Prevention</li>
      <li>Competitive Performance</li>
      <li>Employee moral</li>
    </ul>
  </div>
  <div class="block" style="top:306px;left:26px">
    <h2 class="heading">Service Capabilities</h2>
    <ul class="bullets spaced" style="margin-top:5px">
      <li>Collection Training and Seminars</li>
      <li>Payment Monitoring</li>
      <li>Free Online Collection Account Access</li>
      <li>Credit Bureau Reporting</li>
      <li>Electronic Payment Solutions</li>
      <li>Skip Tracing Services</li>
      <li>Automated On-line Payment Reporting</li>
      <li>Friendly Reminder Notices</li>
      <li>All credit cards accepted</li>
    </ul>
  </div>
</section>

<section class="page page--leadership">
  <div class="block" style="top:18px">
    <h2 class="heading">Leadership</h2>
    <p class="subtitle">Key Personnel</p>

    <div class="person">
      <h3 class="person-name">Daniel Whitmore</h3>
      <p class="person-role">Chief Executive Office</p>
      <p class="body-text">Dan founded KTR in 1986 and remains involved in the day to day operations at KTR. As CEO his primary responsibility his the high- level strategic operations for the company. As a hands-on leader, he is equally at home working directly with employees to foster excellence throughout the entire company. Through Dan's leadership KTR has grown from a small, local collection agency to a company with a sound reputation and clients throughout the U.S.</p>
    </div>
    <div class="person">
      <h3 class="person-name">Daniel Whitmore II</h3>
      <p class="person-role">Chief Financial Offier</p>
      <p class="body-text">Daniel KTR in 2009. He is directly respostible for KTR's finance and compliance. Among his responsibilities, he oversees bookkeeping and trust account reconciliation, analyzes credit statistics capital structure, and other financial information.<br>Daniel bgain his career in finance in 2005 with Harbor Point Securities in New York as in investment banking analyst. In 2006 he joined Meridian Asset Management as a Hedge Fund Analyst in Distressed Credit Strategies. He hold's a bachelor of ARTS degree in Economics from Linden College in Lindenfield, MA.</p>
    </div>
    <div class="person">
      <h3 class="person-name">Bryce Lee Whitmore</h3>
      <p class="body-text">Bryce joined KTR in 2002 first as a collector and then as a sales represented. He was promoted to his current role in 2006 where he oversees all collections activity. Bryce responsibilities include: recruiting, training, and managing all collection associations/<br>Bryce also manages all hardware, software, and outbound call functions. He builds and manages account flow procedures within collection software as well as audits collection files. In addition, he listens to call recordings with collection representatives to ensure quality and compliance.</p>
    </div>
    <div class="person">
      <h3 class="person-name">Laura Bennett</h3>
      <p class="body-text">Laura joined KTR in 2018 bringing over 20 years of management and executive experience in service-based industries; Laura holds a Bachelor of Arts in Business Administration from Cascade University of Spokane, Washington.<br>Laura is responsible for ensuring the integration of key initiatives company wide. Including those for administration, client services, sales, marketing, recruiting, retention, and compliance. She is responsible for process improvement and proactively develops systems designed to maximize business efficiency.</p>
    </div>
    <div class="person">
      <h3 class="person-name">Megan Holloway</h3>
      <p class="body-text">Megan joined KTR in 1998 and has been instrumental in the growth and development of the company. Megan works directly with clients to answer day-to-day questions about accounts. Including providing statements, connectivity, with our client site, and information about specific accounts.<br>Megan oversees all administrative functions of the company for client's services. She is also able to initiate requests for customized reporting or other special projects</p>
    </div>
  </div>
</section>

<section class="page page--values">
  <div class="block" style="top:20px">
    <h2 class="heading">Core Values</h2>
    <div class="value-badges">
      <div class="value-badge" role="img" aria-label="Hand-lettered value: Be Engaged" style="background:linear-gradient(135deg,#f4a3b8,#e8473f)"></div>
      <div class="value-badge" role="img" aria-label="Hand-lettered value: Follow Through" style="background:linear-gradient(135deg,var(--yellow),#f5b81f)"></div>
      <div class="value-badge" role="img" aria-label="Hand-lettered value: Think First" style="background:radial-gradient(circle,#f7c637,#e2571e)"></div>
      <div class="value-badge" role="img" aria-label="Hand-lettered value: Be Respectful" style="background:linear-gradient(135deg,#fdf3ea,#f0b995)"></div>
      <div class="value-badge value-badge--tag" role="img" aria-label="Name-tag style value: Accountable"></div>
    </div>
  </div>
  <div class="block" style="top:120px">
    <h2 class="heading">The KTR Difference</h2>
    <p class="subheading">Quality and Excellence</p>
    <p class="body-text" style="margin-top:10px">Once again, we hope that you will give us the opportunity to work with you to tailor a program that will enable us to deliver on your definisition of the ideal agency partnership.<br>Our pledge is to work shoulder-shoulder with you to build the agency relationship that you want.<br>That is what defines who we are as an organization<br>That is the KTR Differences</p>
    <p class="contact" style="margin-top:10px">
      <strong>Your Receivables Management Partner</strong>
      (800) 555-0142<br>
      4520 Alder Ridge Way<br>
      Suite 310 Marysville, WA<br>
      ktrv.net
    </p>
  </div>
  <div class="illustration" role="img" aria-label="Flat illustration of two people working at laptops on a desk with coffee, notebooks, charts and a calculator"></div>
</section>

</body>
</html>
```